Financial firm simple design

Classic business card design for a financial fund. 2 sided card- white on both sides.. One with just the company name centered and the other w the info. info included on that is :

Name
Company position
phone number
fax
email
website

Industry/Entity Type

Financial

```html
<!DOCTYPE html>
<html lang="en">
<head>
<meta charset="utf-8">
<title>RMK Investments — Business Card</title>
<link rel="stylesheet" href="https://fonts.googleapis.com/css2?family=Cinzel:wght@400&family=Arimo:wght@400&display=swap">
<style>
  :root {
    --stage: #d4d4d4;
    --card: #ffffff;
    --navy: #1b3f73;
    --charcoal: #353535;
    --ink: #111111;
    --rule: #9fb1cc;
  }
  * { margin: 0; padding: 0; box-sizing: border-box; }
  html, body {
    width: 900px;
    height: 1200px;
    overflow: hidden;
    background: var(--stage);
  }
  .card {
    position: absolute;
    left: 143px;
    width: 633px;
    background: var(--card);
    overflow: hidden;
  }
  .card--front { top: 138px; height: 378px; }
  .card--back  { top: 670px; height: 375px; }

  .wordmark {
    font-family: "Cinzel", "Times New Roman", serif;
    font-weight: 400;
    color: var(--navy);
    white-space: nowrap;
    line-height: 1;
  }
  .card--front .wordmark {
    position: absolute;
    left: 0; right: 0;
    top: 154px;
    text-align: center;
    font-size: 38px;
    letter-spacing: 2px;
  }

  .header-row {
    position: absolute;
    left: 0; right: 0;
    top: 66px;
    display: flex;
    align-items: center;
  }
  .header-row .rule {
    height: 1px;
    background: var(--rule);
  }
  .header-row .rule--left { width: 57px; }
  .header-row .rule--right { flex: 1; }
  .header-row .wordmark {
    font-size: 24px;
    letter-spacing: 1.2px;
    padding: 0 8px 0 6px;
  }

  .band {
    position: absolute;
    left: 0; right: 0; bottom: 0;
    display: flex;
  }
  .card--front .band { height: 9px; }
  .card--back .band { height: 12px; }
  .band .seg--dark { background: var(--charcoal); }
  .band .seg--navy { background: var(--navy); }
  .card--front .band .seg--dark { width: 215px; }
  .card--front .band .seg--navy { flex: 1; }
  .card--back .band .seg--navy { width: 408px; }
  .card--back .band .seg--dark { flex: 1; }

  .contact {
    position: absolute;
    left: 406px;
    top: 206px;
    font-family: "Arimo", Arial, sans-serif;
    color: var(--ink);
  }
  .contact .name {
    font-size: 19px;
    color: var(--navy);
    line-height: 22px;
  }
  .contact .role {
    font-size: 14px;
    line-height: 20px;
    margin-bottom: 10px;
  }
  .contact .details {
    list-style: none;
    font-size: 12.5px;
    line-height: 19px;
  }
</style>
</head>
<body>
  <section class="card card--front" aria-label="Card front">
    <div class="wordmark">RMK Investments</div>
    <div class="band"><span class="seg seg--dark"></span><span class="seg seg--navy"></span></div>
  </section>

  <section class="card card--back" aria-label="Card back">
    <div class="header-row">
      <span class="rule rule--left"></span>
      <span class="wordmark">RMK Investments</span>
      <span class="rule rule--right"></span>
    </div>
    <div class="contact">
      <p class="name">Arjun Mehta</p>
      <p class="role">CEO</p>
      <ul class="details">
        <li>phone - 0381557204</li>
        <li>fax- 8827340192</li>
        <li>email- arjunmehta@mailbox.com</li>
        <li>website- www. arjunmehta.com</li>
      </ul>
    </div>
    <div class="band"><span class="seg seg--navy"></span><span class="seg seg--dark"></span></div>
  </section>
</body>
</html>
```